Upsell Vertical Banner Ad Design For B2B Marketing Agency Vertical 768px × 1180px IS THE SIZE

I need a banner made for my website www.brightlanepromotionhub.biz This banner will be an upsell advertisement for after someone signs up for my monthly program. When they login to their account for the 1st time I will give them the chance to upgrade their account to our annual program with just one click.

this is a page that upsells it currently to give you an idea how we market ourselves:
https://tlpx.pagevault-example.com/page/tlp-annual-upsell

Use this content:

Are You Ready To Commit To Taking Your Business To The Next Level?

Because We're In This For The Long-Haul and Dedicated To Your Success...

Save $300 By Upgrading To An Annual Membership And Pay Only $74/mth

((BUTTON))Yes, Upgrade My Plan Right Now!

*Must prepay the full year at only $898/yr!

Target Market(s)

business owners

Industry/Entity Type

Marketing

Requirements
Must have
• 768px × 1180px IS THE SIZE vertical

Use this content:

Nice to have
• Use this content:

Should not have
• Use this content:

```html
<!DOCTYPE html>
<html lang="en">
<head>
<meta charset="utf-8">
<title>Bright Lane Promotion Hub – Annual Upgrade Banner</title>
<link rel="stylesheet" href="https://fonts.googleapis.com/css2?family=Outfit:wght@300;400;600;700&display=swap">
<style>
  :root {
    --brand-blue: #1275bd;
    --ink-gray: #4d4d4f;
    --paper: #f7f7f7;
    --paper-light: #ffffff;
    --stage: #dcdcdc;
    --road-dark: #535456;
    --road-soft: rgba(83, 84, 86, 0);
    --white: #ffffff;
  }
  * { margin: 0; padding: 0; box-sizing: border-box; }
  html, body {
    width: 813px;
    height: 1200px;
    overflow: hidden;
    background: var(--stage);
    font-family: "Outfit", sans-serif;
  }
  .banner {
    position: absolute;
    left: 22px;
    top: 10px;
    width: 768px;
    height: 1180px;
    overflow: hidden;
    background: linear-gradient(180deg, var(--paper) 0%, var(--paper-light) 60%, var(--paper) 100%);
    color: var(--ink-gray);
  }
  .road-art {
    position: absolute;
    left: 0;
    top: 640px;
    width: 768px;
    height: 540px;
    background: linear-gradient(180deg, var(--road-soft) 0%, rgba(83, 84, 86, 0.15) 40%, var(--road-dark) 75%, var(--road-dark) 100%);
  }
  .brand {
    position: absolute;
    left: 48px;
    top: 46px;
    display: flex;
    align-items: center;
    gap: 16px;
  }
  .brand-dot {
    width: 40px;
    height: 40px;
    border-radius: 50%;
    background: var(--brand-blue);
  }
  .brand-name {
    font-weight: 600;
    font-size: 34px;
    letter-spacing: 1px;
    color: var(--brand-blue);
    text-transform: uppercase;
  }
  .headline {
    position: absolute;
    left: 46px;
    top: 204px;
    text-transform: uppercase;
    line-height: 1;
  }
  .headline span { display: block; white-space: nowrap; }
  .headline .thin-gray { font-weight: 300; font-size: 60px; color: var(--ink-gray); }
  .headline .bold-blue { font-weight: 700; font-size: 44px; color: var(--brand-blue); margin-top: 8px; letter-spacing: -0.5px; }
  .headline .wide-gray { font-weight: 300; font-size: 58px; color: var(--ink-gray); letter-spacing: 3px; margin-top: 4px; }
  .headline .final-line { font-size: 56px; color: var(--brand-blue); margin-top: 4px; }
  .headline .final-line .thin { font-weight: 300; display: inline; }
  .headline .final-line .strong { font-weight: 700; display: inline; letter-spacing: -1px; }
  .question-mark {
    position: absolute;
    left: 540px;
    top: 128px;
    font-weight: 700;
    font-size: 360px;
    line-height: 1;
    color: var(--brand-blue);
  }
  .reassurance {
    position: absolute;
    left: 48px;
    top: 466px;
    font-weight: 600;
    font-size: 26px;
    line-height: 34px;
    letter-spacing: -0.3px;
    color: var(--ink-gray);
  }
  .savings {
    position: absolute;
    left: 44px;
    top: 548px;
    font-weight: 700;
    font-size: 90px;
    line-height: 1;
    letter-spacing: -1px;
    color: var(--brand-blue);
  }
  .offer {
    position: absolute;
    left: 48px;
    top: 648px;
    font-weight: 600;
    font-size: 24px;
    line-height: 35px;
    letter-spacing: -0.3px;
    color: var(--ink-gray);
  }
  .cta-button {
    position: absolute;
    left: 48px;
    top: 746px;
    width: 362px;
    height: 102px;
    border-radius: 10px;
    background: var(--brand-blue);
    color: var(--white);
    text-align: center;
    text-transform: uppercase;
    text-decoration: none;
    font-weight: 700;
    padding-top: 12px;
    line-height: 1;
  }
  .cta-button .cta-main { display: block; font-size: 44px; letter-spacing: -1px; }
  .cta-button .cta-sub { display: block; font-size: 30px; letter-spacing: -0.8px; margin-top: 2px; }
  .fine-print {
    position: absolute;
    left: 48px;
    top: 858px;
    font-weight: 300;
    font-size: 16px;
    color: #222;
  }
</style>
</head>
<body>
  <main class="banner">
    <div class="road-art" role="img" aria-label="Illustration of a road rising into an upward arrow, painted with the words Next Level"></div>

    <header class="brand">
      <span class="brand-dot"></span>
      <span class="brand-name">Bright Lane Promotion Hub</span>
    </header>

    <h1 class="headline">
      <span class="thin-gray">Are You Ready</span>
      <span class="bold-blue">To Commit To Taking</span>
      <span class="wide-gray">Your Business</span>
      <span class="final-line"><span class="thin">To The </span><span class="strong">Next Level</span></span>
    </h1>
    <div class="question-mark" aria-hidden="true">?</div>

    <p class="reassurance">Because We're In This For The Long-Haul<br>and Dedicated To Your Success...</p>

    <p class="savings">SAVE $300</p>
    <p class="offer">By Upgrading To An Annual Membership<br>And Pay Only $74/mth</p>

    <a class="cta-button" href="https://tlpx.pagevault-example.com/page/tlp-annual-upsell">
      <span class="cta-main">Yes, Upgrade</span>
      <span class="cta-sub">My Plan Right Now!</span>
    </a>

    <p class="fine-print">*Must prepay the full year at only $898/yr!</p>
  </main>
</body>
</html>
```